Semi-anonymous photo sharing and messaging app

Design app interface. App is needed for semi-anonymous communication.

For instance if you are on a tour bus, and you just met some people there. You want to send them pictures, but you don't want to give your plimora / email / phone number. So instead you use this app - current name is "eMilto" but you can also suggest a name if it fits really well with the theme of the design.

The initial version of the app is in the vonder store
https://shop.vanterix.net/store/apps/details?id=com.k7rwpzlm3qe9yhtab2xcu

the web version of this app is located here
https://bluekettlepath.net/

it is called Brisk Lantern Tide, because the password is four common words, and if you know those words, you can open the chat room.

As you can see app looks very poorly, and needs to be designed from bottom up. App should look nothing like it looks now. it should have original and easily recognizable feel to it.

I'm attaching screen-shots of the current app. Two screens - you enter password on one screen (or choose one of the existing "rooms") - you chat with peers on the second screen

It should be something neutral, so it's mainly for travellers, but could be used by anyone else. It should have vibe of comfort and security, but at the same time adventure and fun.

Please come back with more questions!

Target Market(s)

Travellers, mostly
single, groups,

Industry/Entity Type

Communication

Font styles to use
Sans Serif

Requirements
Must have
• original, light feel
• recognizable
• unique

```html
<!DOCTYPE html>
<html lang="en">
<head>
<meta charset="utf-8">
<title>Join My Group Now – Chat</title>
<link rel="stylesheet" href="https://fonts.googleapis.com/css2?family=Varela+Round&family=Noto+Sans:wght@400&family=Roboto:wght@400&display=swap">
<style>
  :root {
    --status-teal: #40b6a2;
    --bar-teal: #4ec4b1;
    --hex-teal: #47baa5;
    --mint-bubble: #98f7e7;
    --white: #ffffff;
    --ink: #1b1b1b;
    --olive: #9b995c;
    --subbar: #6b8a78;
    --chat-dark: #3b5f4f;
    --chat-mid: #4f7563;
    --chat-olive: #5b7a52;
    --kb-bg: #eceff1;
    --kb-line: #d5d9dc;
    --key-ink: #37474f;
    --key-hint: #5f6b72;
    --space-bar: #d0d5d8;
  }
  * { box-sizing: border-box; margin: 0; padding: 0; }
  html, body { width: 675px; height: 1200px; overflow: hidden; background: #fff; }
  .screen { position: relative; width: 675px; height: 1200px; overflow: hidden; font-family: "Noto Sans", sans-serif; }

  .status-bar { position: absolute; left: 0; top: 0; width: 675px; height: 46px; background: var(--status-teal); color: var(--white); }
  .status-bar svg { position: absolute; }
  .status-time { position: absolute; right: 12px; top: 6px; font-family: "Roboto", sans-serif; font-size: 29px; }

  .app-bar { position: absolute; left: 0; top: 46px; width: 675px; height: 95px; background: var(--bar-teal); color: var(--white); font-family: "Varela Round", sans-serif; }
  .app-bar .back { position: absolute; left: 28px; top: 30px; }
  .app-title { position: absolute; left: 103px; top: 28px; font-size: 32px; letter-spacing: 1px; }
  .exit { position: absolute; right: 26px; top: 33px; font-size: 28px; letter-spacing: 0.5px; }

  .chat-area { position: absolute; left: 0; top: 141px; width: 675px; height: 672px;
    background:
      radial-gradient(ellipse 260px 200px at 90px 520px, rgba(120,140,80,0.55), transparent 70%),
      radial-gradient(ellipse 300px 260px at 600px 480px, rgba(110,150,140,0.45), transparent 70%),
      radial-gradient(ellipse 320px 200px at 330px 330px, rgba(90,130,110,0.35), transparent 70%),
      linear-gradient(180deg, var(--chat-mid) 0%, var(--chat-dark) 30%, var(--chat-mid) 70%, var(--chat-olive) 100%);
  }
  .message-count { position: absolute; left: 0; top: 0; width: 675px; height: 54px; background: var(--subbar); color: var(--white); text-align: center; font-size: 27px; line-height: 54px; font-family: "Varela Round", sans-serif; letter-spacing: 0.5px; }

  .avatar { position: absolute; width: 86px; height: 96px; }
  .avatar span { position: absolute; inset: 0; display: flex; align-items: center; justify-content: center; text-align: center; color: var(--white); font-family: "Varela Round", sans-serif; font-size: 27px; line-height: 24px; }
  .avatar-user { left: 12px; top: 235px; }
  .avatar-me { left: 571px; top: 419px; }

  .bubble { position: absolute; font-size: 25px; color: var(--ink); line-height: 30px; }
  .bubble svg { position: absolute; left: 0; top: 0; }
  .bubble p { position: relative; }
  .bubble-incoming { left: 110px; top: 260px; width: 354px; height: 106px; }
  .bubble-incoming p { padding: 21px 0 0 37px; }
  .bubble-outgoing { left: 202px; top: 442px; width: 354px; height: 58px; }
  .bubble-outgoing p { padding: 12px 0 0 19px; }

  .composer { position: absolute; left: 17px; top: 590px; width: 572px; height: 66px; }
  .composer svg.field { position: absolute; left: 0; top: 0; }
  .composer-text { position: absolute; left: 11px; top: 15px; font-size: 25px; color: var(--ink); }
  .camera { position: absolute; left: 490px; top: 12px; }
  .send { position: absolute; left: 599px; top: 591px; }

  .keyboard { position: absolute; left: 0; top: 813px; width: 675px; height: 387px; background: var(--kb-bg); font-family: "Roboto", sans-serif; color: var(--key-ink); }
  .suggestions { position: absolute; left: 0; top: 0; width: 675px; height: 50px; border-bottom: 1px solid var(--kb-line); }
  .suggestions i { position: absolute; top: 14px; width: 1px; height: 26px; background: var(--kb-line); }
  .mic { position: absolute; left: 635px; top: 13px; }
  .key { position: absolute; width: 40px; text-align: center; font-size: 30px; transform: translateX(-50%); }
  .key sup { position: absolute; top: -12px; right: -2px; font-size: 13px; color: var(--key-hint); }
  .row1 .key { top: 73px; }
  .row2 .key { top: 158px; }
  .row3 .key { top: 240px; }
  .kb-icon { position: absolute; }
  .sym { position: absolute; left: 11px; top: 330px; font-size: 20px; color: var(--key-hint); }
  .comma { position: absolute; left: 91px; top: 326px; font-size: 30px; }
  .space { position: absolute; left: 132px; top: 328px; width: 416px; height: 26px; border-radius: 3px; background: var(--space-bar); }
  .period { position: absolute; left: 578px; top: 322px; font-size: 30px; }
  .emoji { position: absolute; left: 633px; top: 328px; }
</style>
</head>
<body>
<div class="screen">

  <header class="status-bar">
    <svg width="24" height="22" viewBox="0 0 24 22" style="left:14px;top:12px"><rect x="1.5" y="1.5" width="21" height="19" fill="none" stroke="#fff" stroke-width="2.5"/><path d="M4 17 L9 10 L13 15 L16 12 L20 17 Z" fill="#fff"/></svg>
    <svg width="38" height="28" viewBox="0 0 38 28" style="left:502px;top:10px"><path d="M19 27 L1 8 A27 27 0 0 1 37 8 Z" fill="#fff"/></svg>
    <svg width="28" height="28" viewBox="0 0 28 28" style="left:536px;top:10px"><path d="M27 1 L27 27 L1 27 Z" fill="#fff"/></svg>
    <svg width="16" height="32" viewBox="0 0 16 32" style="left:575px;top:7px"><rect x="5" y="0" width="6" height="3" fill="#fff"/><rect x="0" y="3" width="16" height="29" fill="#fff"/></svg>
    <span class="status-time">4:20</span>
  </header>

  <nav class="app-bar">
    <svg class="back" width="28" height="40" viewBox="0 0 28 40"><path d="M24 3 L6 20 L24 37" fill="none" stroke="#fff" stroke-width="5" stroke-linecap="round" stroke-linejoin="round"/></svg>
    <h1 class="app-title">JOIN MY GROUP NOW</h1>
    <span class="exit">Exit</span>
  </nav>

  <main class="chat-area">
    <div class="message-count">Total Messages : 2</div>

    <div class="avatar avatar-user">
      <svg width="86" height="96" viewBox="0 0 86 96"><path d="M43 2 L84 25 L84 71 L43 94 L2 71 L2 25 Z" fill="var(--hex-teal)"/></svg>
      <span>User<br>1</span>
    </div>
    <div class="bubble bubble-incoming">
      <svg width="354" height="106" viewBox="0 0 354 106"><path d="M0 0 L349 0 Q352 0 352 3 L352 101 Q352 104 349 104 L18 104 Q13 104 13 99 L13 26 Z" fill="var(--mint-bubble)"/></svg>
      <p>Hi, What’s Going on<br>There ?</p>
    </div>

    <div class="avatar avatar-me">
      <svg width="86" height="96" viewBox="0 0 86 96"><path d="M43 2 L84 25 L84 71 L43 94 L2 71 L2 25 Z" fill="var(--hex-teal)"/></svg>
      <span>Me</span>
    </div>
    <div class="bubble bubble-outgoing">
      <svg width="354" height="58" viewBox="0 0 354 58"><path d="M3 0 L352 0 L341 18 L341 53 Q341 56 338 56 L3 56 Q1 56 1 53 L1 3 Q1 0 3 0 Z" fill="var(--white)"/></svg>
      <p>Having Fun...</p>
    </div>

    <div class="composer">
      <svg class="field" width="572" height="66" viewBox="0 0 572 66"><path d="M4 1 L570 1 L555 18 L555 61 Q555 64 552 64 L4 64 Q1 64 1 61 L1 4 Q1 1 4 1 Z" fill="var(--white)"/></svg>
      <span class="composer-text">See you at my place at 18.</span>
      <svg class="camera" width="52" height="40" viewBox="0 0 52 40"><rect x="8" y="1" width="12" height="6" fill="none" stroke="var(--olive)" stroke-width="2.5"/><rect x="2" y="7" width="48" height="31" rx="2" fill="none" stroke="var(--olive)" stroke-width="2.5"/><line x1="2" y1="13" x2="50" y2="13" stroke="var(--olive)" stroke-width="2"/><circle cx="26" cy="24" r="9" fill="none" stroke="var(--olive)" stroke-width="2.5"/><circle cx="26" cy="24" r="4" fill="var(--olive)"/></svg>
    </div>
    <svg class="send" width="64" height="64" viewBox="0 0 64 64"><circle cx="32" cy="32" r="31" fill="var(--olive)"/><path d="M16 32 H44 M33 20 L46 32 L33 44" fill="none" stroke="#fff" stroke-width="6" stroke-linecap="round" stroke-linejoin="round"/></svg>
  </main>

  <section class="keyboard" aria-label="On-screen keyboard">
    <div class="suggestions"><i style="left:236px"></i><i style="left:437px"></i>
      <svg class="mic" width="18" height="26" viewBox="0 0 18 26"><rect x="5" y="1" width="8" height="15" rx="4" fill="var(--key-ink)"/><path d="M2 12 A7 7 0 0 0 16 12" fill="none" stroke="var(--key-ink)" stroke-width="2"/><line x1="9" y1="19" x2="9" y2="25" stroke="var(--key-ink)" stroke-width="2"/></svg>
    </div>
    <div class="row1">
      <span class="key" style="left:30px">Q<sup>1</sup></span>
      <span class="key" style="left:91px">W<sup>2</sup></span>
      <span class="key" style="left:151px">E<sup>3</sup></span>
      <span class="key" style="left:212px">R<sup>4</sup></span>
      <span class="key" style="left:273px">T<sup>5</sup></span>
      <span class="key" style="left:334px">Y<sup>6</sup></span>
      <span class="key" style="left:395px">U<sup>7</sup></span>
      <span class="key" style="left:456px">I<sup>8</sup></span>
      <span class="key" style="left:517px">O<sup>9</sup></span>
      <span class="key" style="left:577px">P<sup>0</sup></span>
      <svg class="kb-icon" style="left:627px;top:82px" width="30" height="22" viewBox="0 0 30 22"><path d="M9 1 H29 V21 H9 L1 11 Z" fill="#8a949a"/><path d="M14 6 L23 16 M23 6 L14 16" stroke="#fff" stroke-width="2.5"/></svg>
    </div>
    <div class="row2">
      <span class="key" style="left:60px">A</span>
      <span class="key" style="left:121px">S</span>
      <span class="key" style="left:182px">D</span>
      <span class="key" style="left:243px">F</span>
      <span class="key" style="left:304px">G</span>
      <span class="key" style="left:364px">H</span>
      <span class="key" style="left:425px">J</span>
      <span class="key" style="left:486px">K</span>
      <span class="key" style="left:547px">L</span>
      <svg class="kb-icon" style="left:605px;top:156px" width="42" height="42" viewBox="0 0 42 42"><circle cx="21" cy="21" r="20" fill="var(--bar-teal)"/><path d="M29 14 V23 H13 M18 18 L13 23 L18 28" fill="none" stroke="#fff" stroke-width="2.5"/></svg>
    </div>
    <div class="row3">
      <svg class="kb-icon" style="left:20px;top:247px" width="26" height="44" viewBox="0 0 26 44"><path d="M13 2 L25 16 H18 V24 H8 V16 H1 Z" fill="var(--bar-teal)"/><line x1="3" y1="42" x2="23" y2="42" stroke="#5f6b72" stroke-width="2"/></svg>
      <span class="key" style="left:96px">Z</span>
      <span class="key" style="left:157px">X</span>
      <span class="key" style="left:218px">C</span>
      <span class="key" style="left:279px">V</span>
      <span class="key" style="left:340px">B</span>
      <span class="key" style="left:401px">N</span>
      <span class="key" style="left:462px">M</span>
      <span class="key" style="left:522px">!</span>
      <span class="key" style="left:583px">?</span>
      <svg class="kb-icon" style="left:631px;top:247px" width="26" height="44" viewBox="0 0 26 44"><path d="M13 2 L25 16 H18 V24 H8 V16 H1 Z" fill="var(--bar-teal)"/><line x1="3" y1="42" x2="23" y2="42" stroke="#5f6b72" stroke-width="2"/></svg>
    </div>
    <span class="sym">?123</span>
    <span class="comma">,</span>
    <span class="space"></span>
    <span class="period">.</span>
    <svg class="emoji" width="24" height="24" viewBox="0 0 24 24"><circle cx="12" cy="12" r="10.5" fill="none" stroke="var(--key-ink)" stroke-width="2"/><circle cx="8.5" cy="9.5" r="1.5" fill="var(--key-ink)"/><circle cx="15.5" cy="9.5" r="1.5" fill="var(--key-ink)"/><path d="M7 14 Q12 19 17 14" fill="none" stroke="var(--key-ink)" stroke-width="2"/></svg>
  </section>

</div>
</body>
</html>
```